Clinical Research Consulting Company needs a web design

My consulting company provides service on clinical trial design and clincal research, product safety and claim development strategy, and lecture service.

Need template and graphic design for the website of my consulting company. Website will have many different tabs (e.g., Home, About Us, Service, and Contact Us).

Like to have modern look and easy on eyes (not too many colors).

We don't perform laboratory work so please do not use pictures with people working in the laboratory. Also, the logo is added. Thanks.

Target Market(s)

Pharmaceutical and Biotech companies, dietary supplement companies, food industry

Industry/Entity Type

It Company

Number of Pages Required

4 page

Font styles to use
Sans Serif

Requirements
Must have
• hyperlink to Contact Us page
Nice to have
• pictures

```html
<!DOCTYPE html>
<html lang="en">
<head>
<meta charset="utf-8">
<title>Corvane Consulting Inc</title>
<link href="https://fonts.googleapis.com/css2?family=Dosis:wght@300;400;500;600&family=Open+Sans:wght@400&display=swap" rel="stylesheet">
<style>
:root{
  --accent:#49b8d9;
  --dark:#2f3236;
  --ink:#2b2b2b;
  --muted:#8e8e8e;
  --topbar:#f2f2f2;
  --band:#f9f9f9;
  --line:#d8d8d8;
  --white:#ffffff;
}
*{box-sizing:border-box;margin:0;padding:0}
html,body{width:854px;height:1200px;overflow:hidden;background:var(--white)}
body{position:relative;font-family:'Dosis',sans-serif;color:var(--ink)}
.abs{position:absolute}
a{color:inherit;text-decoration:none}

.topbar{left:0;top:0;width:854px;height:24px;background:var(--topbar);font-size:10px;font-family:'Open Sans',sans-serif}
.topbar .social-dot{top:8px;width:7px;height:7px;border-radius:50%;background:var(--ink)}
.topbar .link{top:6px}
.topbar .sep{top:6px;width:1px;height:12px;background:var(--line)}
.topbar .contact{top:6px;display:flex;align-items:center;gap:6px}

.header{left:0;top:24px;width:854px;height:58px;background:var(--white)}
.brand{left:123px;top:17px;font-size:20px;font-weight:400;color:var(--ink)}
.nav{top:22px;font-size:11px;font-family:'Open Sans',sans-serif;color:var(--ink)}
.nav.active{color:var(--accent)}

.hero{left:0;top:82px;width:854px;height:243px;background:linear-gradient(90deg,#b9bcbc 0%,#d9dcd9 35%,#e9ebe8 55%,#dde0de 75%,#c7b99c 100%)}
.hero-title{left:124px;top:120px;font-size:26px;font-weight:600;line-height:30px;color:#2d2d2d}
.hero-title span{color:var(--accent)}
.hero-text{left:124px;top:216px;font-size:12px;line-height:14px;color:#3a3a3a;width:310px}
.btn{display:flex;align-items:center;justify-content:space-between;background:var(--dark);color:var(--white);font-size:9px;text-transform:uppercase;padding:0 10px 0 8px;border:1px solid #5a6066}
.btn.alt{background:var(--accent);border-color:var(--accent)}
.hero-btn{left:122px;top:270px;width:136px;height:34px}
.dots{left:413px;top:305px;display:flex;gap:5px}
.dots i{width:5px;height:5px;border-radius:50%;background:rgba(255,255,255,.6)}
.dots i:first-child{background:var(--white)}

.welcome{left:0;top:342px;width:854px;text-align:center;font-size:24px;font-weight:300}
.welcome span{color:var(--accent);font-weight:400}
.rule{left:392px;top:379px;width:71px;height:3px;background:var(--accent)}
.kicker{left:0;top:391px;width:854px;text-align:center;font-size:10px;font-weight:500}

.card{top:428px;width:146px;height:183px;border-bottom:2px solid var(--accent)}
.card .photo{width:146px;height:132px}
.card h3{position:absolute;top:141px;left:2px;font-size:10px;font-weight:500}
.card .chev{position:absolute;top:142px;right:2px}
.card p{position:absolute;top:158px;left:1px;font-family:'Open Sans',sans-serif;font-size:7px;line-height:9px;color:var(--muted)}

.services{left:0;top:650px;width:854px;height:187px;background:var(--band);border-top:1px solid #efefef}
.service{top:672px;width:150px;text-align:center}
.service svg{display:block;margin:0 auto}
.service h3{margin-top:14px;font-size:13px;font-weight:500}
.service p{margin-top:4px;font-family:'Open Sans',sans-serif;font-size:7px;line-height:9px;color:#555}
.apply{top:802px;width:95px;height:35px}

.contact-title{left:130px;top:906px;font-size:18px;font-weight:500}
.field{height:24px;border:1px solid var(--line);font-size:8px;color:#777;padding:7px 9px;font-family:'Open Sans',sans-serif;background:var(--white)}
.send{left:610px;top:939px;width:105px;height:24px;background:var(--accent);color:var(--white);font-size:11px;text-align:center;line-height:24px}
.social-title{left:129px;top:1051px;font-size:18px;font-weight:500}
.social-dot-lg{top:1081px;width:20px;height:20px;border-radius:50%}
.location{left:451px;top:1044px;width:80px;height:78px;background:#333;color:var(--white);text-align:center;font-size:14px}
.map{left:531px;top:1044px;width:183px;height:78px;background:linear-gradient(135deg,#e6e3dc,#d9d6cf)}

.footer{left:0;top:1145px;width:854px;height:55px;background:var(--accent);color:var(--white)}
.footer .copy{left:124px;top:22px;font-size:10px;font-family:'Open Sans',sans-serif}
.footer .brand-foot{left:564px;top:17px;font-size:18px;font-weight:300}
</style>
</head>
<body>

<div class="abs topbar">
  <span class="abs social-dot" style="left:122px"></span>
  <span class="abs social-dot" style="left:144px"></span>
  <span class="abs sep" style="left:159px"></span>
  <a class="abs link" href="#" style="left:167px">Log In</a>
  <span class="abs sep" style="left:197px"></span>
  <a class="abs link" href="#" style="left:204px">Sign Up</a>
  <div class="abs contact" style="left:525px">
    <svg width="11" height="11" viewBox="0 0 24 24"><path d="M6.6 10.8a15 15 0 0 0 6.6 6.6l2.2-2.2a1 1 0 0 1 1-.25 11.4 11.4 0 0 0 3.6.57 1 1 0 0 1 1 1V20a1 1 0 0 1-1 1A17 17 0 0 1 3 4a1 1 0 0 1 1-1h3.5a1 1 0 0 1 1 1c0 1.25.2 2.45.57 3.57a1 1 0 0 1-.25 1z" fill="#49b8d9"/></svg>
    <span>0800-555-0192</span>
  </div>
  <div class="abs contact" style="left:615px">
    <svg width="12" height="9" viewBox="0 0 12 9"><rect x="0.5" y="0.5" width="11" height="8" fill="none" stroke="#49b8d9"/><path d="M0.5 0.5 6 5 11.5 0.5" fill="none" stroke="#49b8d9"/></svg>
    <span>hello@corvaneconsulting.com</span>
  </div>
</div>

<header class="abs header">
  <div class="abs brand">Corvane Consulting Inc</div>
  <a class="abs nav active" href="#" style="left:453px">Home</a>
  <a class="abs nav" href="#" style="left:513px">About</a>
  <a class="abs nav" href="#" style="left:574px">Services</a>
  <a class="abs nav" href="#" style="left:645px">Blog</a>
  <a class="abs nav" href="#contact" style="left:700px">Contact</a>
</header>

<section class="abs hero" role="img" aria-label="Photo of a doctor in a white coat holding a tablet showing the company name, in a bright clinic"></section>
<h1 class="abs hero-title">Leading global consulting<br>firm <span>focused exclusively on<br>life sciences</span></h1>
<p class="abs hero-text">We are passionate about supporting our clients as they create ground-breaking treatments and improve health all over the world</p>
<a class="abs btn hero-btn" href="#">Get register now
  <svg width="20" height="20" viewBox="0 0 20 20"><circle cx="10" cy="10" r="9" fill="none" stroke="#fff"/><path d="M5.5 10h9M11 6.5 14.5 10 11 13.5" fill="none" stroke="#fff"/></svg>
</a>
<div class="abs dots"><i></i><i></i><i></i></div>

<h2 class="abs welcome">WELCOME TO THE <span>CORVANE CONSULTING INC</span></h2>
<div class="abs rule"></div>
<p class="abs kicker">CATAGORIES : CHOOSE YOUR OPTION !</p>

<article class="abs card" style="left:128px">
  <div class="photo" role="img" aria-label="Photo of sample vials in a blue-lit rack" style="background:linear-gradient(160deg,#1f5f9c,#3d9ddc 60%,#c9e6f6)"></div>
  <h3>PHARMACEUTICAL COMPANIES</h3>
  <svg class="chev" width="6" height="9" viewBox="0 0 6 9"><path d="M1 1l3.5 3.5L1 8" fill="none" stroke="#49b8d9" stroke-width="1.5"/></svg>
  <p>Lorem ipsum dolor sit amet, consectetu<br>adipiscing elit, sed diam</p>
</article>
<article class="abs card" style="left:282px">
  <div class="photo" role="img" aria-label="Photo of a gloved hand holding a dish with a green seedling" style="background:linear-gradient(150deg,#3b4fb0,#7d8fd8 55%,#c7d0ee)"></div>
  <h3>BIOTECH COMPANIES</h3>
  <svg class="chev" width="6" height="9" viewBox="0 0 6 9"><path d="M1 1l3.5 3.5L1 8" fill="none" stroke="#49b8d9" stroke-width="1.5"/></svg>
  <p>Lorem ipsum dolor sit amet, consectetu<br>adipiscing elit, sed diam</p>
</article>
<article class="abs card" style="left:436px">
  <div class="photo" role="img" aria-label="Photo of store shelves stocked with supplement bottles" style="background:linear-gradient(90deg,#6b5a3e,#b8955f 50%,#8d6b45)"></div>
  <h3>DIETARY SUPPLEMENT FIRMS</h3>
  <svg class="chev" width="6" height="9" viewBox="0 0 6 9"><path d="M1 1l3.5 3.5L1 8" fill="none" stroke="#49b8d9" stroke-width="1.5"/></svg>
  <p>Lorem ipsum dolor sit amet, consectetu<br>adipiscing elit, sed diam</p>
</article>
<article class="abs card" style="left:591px">
  <div class="photo" role="img" aria-label="Photo of a food processing factory line" style="background:linear-gradient(180deg,#6f7477,#9a9c98 50%,#b48e4e)"></div>
  <h3>FOOD INDUSTRY</h3>
  <svg class="chev" width="6" height="9" viewBox="0 0 6 9"><path d="M1 1l3.5 3.5L1 8" fill="none" stroke="#49b8d9" stroke-width="1.5"/></svg>
  <p>Lorem ipsum dolor sit amet, consectetu<br>adipiscing elit, sed diam</p>
</article>

<section class="abs services"></section>
<div class="abs service" style="left:121px">
  <svg width="44" height="50" viewBox="0 0 44 50"><circle cx="12" cy="7" r="5" fill="#49b8d9"/><rect x="3" y="14" width="17" height="34" rx="3" fill="#49b8d9"/><path d="M26 16l14 4v10c0 9-6 14-14 18-8-4-14-9-14-18V20z" fill="#49b8d9" stroke="#f9f9f9" stroke-width="2"/><path d="M26 20v24c6-3 10-7 10-14v-7z" fill="#f9f9f9"/></svg>
  <h3>INSURANCE</h3>
  <p>Lorem ipsum dolor sit amet, consectetu<br>adipiscing elit, sed diam</p>
</div>
<div class="abs service" style="left:279px">
  <svg width="48" height="50" viewBox="0 0 48 50"><rect x="3" y="36" width="5" height="12" fill="#49b8d9"/><rect x="11" y="32" width="5" height="16" fill="#49b8d9"/><rect x="19" y="28" width="5" height="20" fill="#49b8d9"/><rect x="27" y="24" width="5" height="24" fill="#49b8d9"/><rect x="35" y="18" width="5" height="30" fill="#49b8d9"/><path d="M2 30C16 28 28 20 36 10" fill="none" stroke="#49b8d9" stroke-width="4"/><path d="M30 8l12-6-2 13z" fill="#49b8d9"/></svg>
  <h3>FINANCIAL</h3>
  <p>Lorem ipsum dolor sit amet, consectetu<br>adipiscing elit, sed diam</p>
</div>
<div class="abs service" style="left:429px">
  <svg width="50" height="50" viewBox="0 0 50 50"><circle cx="24" cy="26" r="23" fill="#49b8d9"/><circle cx="24" cy="26" r="15" fill="#f9f9f9"/><circle cx="24" cy="26" r="10" fill="#49b8d9"/><circle cx="24" cy="26" r="4" fill="#f9f9f9"/><path d="M24 26L44 6" stroke="#49b8d9" stroke-width="3"/><path d="M40 2h8v8z" fill="#49b8d9"/></svg>
  <h3>PLANNING</h3>
  <p>Lorem ipsum dolor sit amet, consectetu<br>adipiscing elit, sed diam</p>
</div>
<div class="abs service" style="left:586px">
  <svg width="44" height="50" viewBox="0 0 44 50"><rect x="3" y="1" width="38" height="48" fill="#49b8d9"/><rect x="6" y="1" width="3" height="48" fill="#f9f9f9" opacity=".6"/><path d="M34 6h4M34 10h4M34 14h4M34 18h4M34 22h4M34 26h4M34 30h4M34 34h4M34 38h4M34 42h4" stroke="#f9f9f9" stroke-width="1"/></svg>
  <h3>ONLINE LECTURE</h3>
  <p>Lorem ipsum dolor sit amet, consectetu<br>adipiscing elit, sed diam</p>
</div>

<a class="abs btn apply" href="#" style="left:148px">Apply now<svg width="20" height="20" viewBox="0 0 20 20"><circle cx="10" cy="10" r="9" fill="none" stroke="#fff"/><path d="M5.5 10h9M11 6.5 14.5 10 11 13.5" fill="none" stroke="#fff"/></svg></a>
<a class="abs btn apply alt" href="#" style="left:307px">Apply now<svg width="20" height="20" viewBox="0 0 20 20"><circle cx="10" cy="10" r="9" fill="none" stroke="#fff"/><path d="M5.5 10h9M11 6.5 14.5 10 11 13.5" fill="none" stroke="#fff"/></svg></a>
<a class="abs btn apply" href="#" style="left:463px">Apply now<svg width="20" height="20" viewBox="0 0 20 20"><circle cx="10" cy="10" r="9" fill="none" stroke="#fff"/><path d="M5.5 10h9M11 6.5 14.5 10 11 13.5" fill="none" stroke="#fff"/></svg></a>
<a class="abs btn apply" href="#" style="left:615px">Apply now<svg width="20" height="20" viewBox="0 0 20 20"><circle cx="10" cy="10" r="9" fill="none" stroke="#fff"/><path d="M5.5 10h9M11 6.5 14.5 10 11 13.5" fill="none" stroke="#fff"/></svg></a>

<h2 class="abs contact-title" id="contact">CONTACT US</h2>
<div class="abs field" style="left:128px;top:939px;width:151px">NAME</div>
<div class="abs field" style="left:289px;top:939px;width:151px">EMAIL</div>
<div class="abs field" style="left:450px;top:939px;width:150px">PHONE NO.</div>
<div class="abs send">SEND</div>
<div class="abs field" style="left:128px;top:970px;width:586px;height:54px">MESSAGE</div>

<h2 class="abs social-title">SOCIAL</h2>
<span class="abs social-dot-lg" style="left:128px;background:#3b5998"></span>
<span class="abs social-dot-lg" style="left:154px;background:#55acee"></span>
<span class="abs social-dot-lg" style="left:181px;background:#dd4b39"></span>
<span class="abs social-dot-lg" style="left:209px;background:#cb2027"></span>

<div class="abs location">
  <svg style="display:block;margin:20px auto 4px" width="14" height="20" viewBox="0 0 14 20"><path d="M7 0a7 7 0 0 0-7 7c0 5 7 13 7 13s7-8 7-13a7 7 0 0 0-7-7z" fill="#49b8d9"/><circle cx="7" cy="7" r="2.5" fill="#333"/></svg>
  LOCATION
</div>
<div class="abs map" role="img" aria-label="Street map showing the office location"></div>

<footer class="abs footer">
  <p class="abs copy">All Rights Reserved. Corvane consulting Inc .© 2015.</p>
  <div class="abs brand-foot">Corvane Consulting Inc</div>
</footer>

</body>
</html>
```